Harbor of Kelvane - Brightleaf Jubilee Poster Design

We need a poster (8.5" x 11") for our Brightleaf Jubilee Celebration event June 18 - 19, 2016. I've included the Port logo, event logo, content, and some photos to choose from. Not all the photos have to be used, though. Feel free to use, crop and size photos how you see fit. Colors and fonts are also up to you. Looking for a fun design that screams family fun event!

Target Market(s)

Families

Industry/Entity Type

Event

Requirements
Must have
• The event logo, the Port logo, some photos (provided) and the content provided.

```html
<!DOCTYPE html>
<html lang="en">
<head>
<meta charset="utf-8">
<title>Brightleaf Jubilee Celebration – Harbor of Kelvane</title>
<link href="https://fonts.googleapis.com/css2?family=Josefin+Sans:wght@400&family=Yellowtail&family=Lobster&family=Roboto+Condensed:ital,wght@0,400;1,700&family=Montserrat:wght@400;700&display=swap" rel="stylesheet">
<style>
  :root {
    --sun: #fcc81a;
    --sky: #86daf6;
    --navy: #1d2a7c;
    --red: #c8242b;
    --rope: #b99a5a;
    --frame: #f7f5ef;
    --photo-a: #8c8a92;
    --photo-b: #7b8a84;
    --photo-c: #6f7d6a;
    --photo-d: #9a9486;
  }
  * { margin: 0; padding: 0; box-sizing: border-box; }
  html, body { width: 927px; height: 1200px; overflow: hidden; background: var(--sky); }
  .poster { position: relative; width: 927px; height: 1200px; background: var(--sky); overflow: hidden; }
  .left-panel { position: absolute; inset: 0; }
  .rope { position: absolute; inset: 0; }

  .event-mark { position: absolute; left: 38px; top: 40px; width: 370px; height: 330px; }
  .event-mark .ring { position: absolute; left: 50px; top: 0; width: 270px; height: 270px; border-radius: 50%; background: var(--sky); border: 22px solid var(--navy); }
  .event-mark .name { position: absolute; left: 0; right: 0; top: 282px; text-align: center; font-family: "Montserrat", sans-serif; font-weight: 700; color: var(--red); font-size: 24px; line-height: 1.15; }

  .rule { position: absolute; left: 84px; width: 272px; height: 2px; background: #fff; }
  .date-block { position: absolute; left: 84px; width: 272px; text-align: center; color: var(--red); font-family: "Josefin Sans", sans-serif; }
  .date-month { top: 410px; font-size: 76px; line-height: 1; letter-spacing: 1px; }
  .date-days { top: 478px; font-size: 82px; line-height: 1; }
  .venue { position: absolute; left: 84px; width: 272px; text-align: center; color: var(--navy); font-family: "Lobster", cursive; }
  .venue-lead { top: 554px; font-size: 24px; }
  .venue-name { top: 578px; font-size: 34px; }

  .schedule { position: absolute; left: 40px; top: 0; width: 330px; font-family: "Roboto Condensed", sans-serif; }
  .day { position: absolute; left: 0; font-family: "Yellowtail", cursive; color: var(--red); font-size: 30px; line-height: 1; white-space: nowrap; }
  .group { position: absolute; left: 0; font-style: italic; font-weight: 700; color: var(--navy); font-size: 18px; line-height: 1; white-space: nowrap; letter-spacing: -0.3px; }
  .item { position: absolute; left: 46px; color: var(--navy); font-size: 17px; line-height: 1; white-space: nowrap; letter-spacing: -0.3px; }
  .item::before { content: "•"; margin-right: 6px; }
  .note { position: absolute; left: 0; color: var(--navy); font-size: 17px; line-height: 1; white-space: nowrap; letter-spacing: -0.3px; }
  .note.indent { left: 48px; font-style: italic; font-weight: 700; font-size: 18px; }
  .note.strong { font-weight: 700; font-style: italic; font-size: 18px; }

  .photo { position: absolute; background: var(--frame); padding: 8px; box-shadow: 0 2px 6px rgba(0,0,0,.25); }
  .photo .fill { width: 100%; height: 100%; }
  .photo-dance { left: 480px; top: 20px; width: 428px; height: 288px; transform: rotate(1deg); }
  .photo-dance .fill { background: linear-gradient(160deg, #a8b0b8, var(--photo-a) 55%, #6b4a5a); }
  .photo-fishing { left: 472px; top: 290px; width: 440px; height: 292px; transform: rotate(-2deg); }
  .photo-fishing .fill { background: linear-gradient(170deg, #a9adb0, var(--photo-b) 50%, #5e6660); }
  .photo-music { left: 436px; top: 570px; width: 428px; height: 254px; transform: rotate(1deg); }
  .photo-music .fill { background: linear-gradient(150deg, var(--photo-c), #8a7a5e 55%, #d9d6cf); }
  .photo-crafts { left: 448px; top: 810px; width: 448px; height: 286px; transform: rotate(-1deg); }
  .photo-crafts .fill { background: linear-gradient(160deg, #54545a, var(--photo-d) 50%, #7a5a3a); }

  .info-band { position: absolute; left: 0; top: 1102px; width: 927px; height: 70px; background: var(--navy); color: #fff; font-family: "Montserrat", sans-serif; text-align: center; padding-left: 150px; }
  .info-band .line-1 { position: absolute; left: 150px; right: 0; top: 11px; font-size: 19px; }
  .info-band .line-2 { position: absolute; left: 150px; right: 0; top: 38px; font-size: 19px; font-weight: 700; }
</style>
</head>
<body>
<main class="poster">
  <svg class="left-panel" width="927" height="1200" viewBox="0 0 927 1200" aria-hidden="true">
    <path d="M0 0 H395 C420 150 390 260 405 400 C420 560 385 700 400 860 C410 980 385 1080 400 1200 H0 Z" fill="var(--sun)"/>
  </svg>
  <svg class="rope" width="927" height="1200" viewBox="0 0 927 1200" role="img" aria-label="Thick twisted rope running down the poster">
    <path d="M385 0 H445 C470 150 440 260 455 400 C470 560 435 700 450 860 C460 980 435 1080 450 1200 H390 C375 1080 400 980 390 860 C375 700 410 560 395 400 C380 260 410 150 385 0 Z" fill="var(--rope)"/>
  </svg>

  <div class="event-mark">
    <div class="ring"></div>
    <div class="name">Brightleaf Jubilee<br>Celebration</div>
  </div>

  <div class="rule" style="top:396px"></div>
  <div class="date-block date-month">JUNE</div>
  <div class="date-block date-days">18–19</div>
  <div class="venue venue-lead">at the</div>
  <div class="venue venue-name">Kelvane Marina</div>
  <div class="rule" style="top:626px"></div>

  <section class="schedule">
    <div class="day" style="top:648px">June 18th</div>
    <div class="group" style="top:688px">Fun for the Whole Family</div>
    <div class="item" style="top:710px">2-for-1 Moorage</div>
    <div class="item" style="top:730px">Live Music</div>
    <div class="item" style="top:750px">Hot Dog Vendor</div>
    <div class="item" style="top:770px">Power Squadron</div>
    <div class="group" style="top:796px">Kid's Activities</div>
    <div class="item" style="top:818px">Fishing Derby</div>
    <div class="item" style="top:838px">Touch a Fire Truck</div>
    <div class="item" style="top:858px">Toy Boat Building</div>
    <div class="group" style="top:884px">Traditional Norwegian Activities</div>
    <div class="item" style="top:906px">Raising the Mai “Green” Stang</div>
    <div class="item" style="top:926px">Traditional Norwegian Food and Dancing</div>
    <div class="item" style="top:946px">Bonfire Lighting with the Kelvane Vikings</div>
    <div class="day" style="top:982px">June 19th</div>
    <div class="note" style="top:1020px">Eldmoor Water Trails Festival –</div>
    <div class="note indent" style="top:1040px">Coves to Cardell Fun Paddle</div>
    <div class="note strong" style="top:1068px">A fun event for paddlers of all levels!</div>
  </section>

  <figure class="photo photo-dance"><div class="fill" role="img" aria-label="Photo of folk dancers in traditional costume circling at the marina"></div></figure>
  <figure class="photo photo-fishing"><div class="fill" role="img" aria-label="Photo of families fishing at a water trough during the derby"></div></figure>
  <figure class="photo photo-music"><div class="fill" role="img" aria-label="Photo of a musician playing acoustic guitar outdoors"></div></figure>
  <figure class="photo photo-crafts"><div class="fill" role="img" aria-label="Photo of children building toy boats at a picnic table"></div></figure>

  <footer class="info-band">
    <p class="line-1">For more information, please call <strong>(555) 014-2290</strong> ext. 1 <em>or</em></p>
    <p class="line-2">www.harborofkelvane.com/jubilee</p>
  </footer>
</main>
</body>
</html>
```